Business card logo

Hello, I would like a business card for my law firm with a logo composed of my initials "CV". The logo is intended to appear on my business card, my letterhead, envelope and documents from my office. My first and last name (Camille Vautrin) and "Lawyer" must appear next to the logo. I would like the logo and the characters to be in golden color on a dark background (example black, navy blue). I would especially like a refined work on the logo which should be composed of the letters J and R.

```html
<!DOCTYPE html>
<html lang="en">
<head>
<meta charset="utf-8">
<title>Camille Vautrin – Lawyer – Business Card</title>
<link rel="stylesheet" href="https://fonts.googleapis.com/css2?family=Cinzel:wght@700&family=Oswald:wght@500&display=swap">
<style>
  :root {
    --page: #ffffff;
    --navy: #032562;
    --gold: #d9b25a;
    --gold-dark: #b07a22;
    --gold-light: #fbed9c;
    --gold-gradient: linear-gradient(90deg, var(--gold-dark) 0%, var(--gold) 40%, var(--gold-light) 75%, var(--gold) 100%);
  }
  * { margin: 0; padding: 0; box-sizing: border-box; }
  html, body {
    width: 1200px;
    height: 858px;
    overflow: hidden;
    background: var(--page);
  }
  .sheet {
    position: relative;
    width: 1200px;
    height: 858px;
  }
  .card {
    position: absolute;
    left: 281px;
    width: 636px;
    height: 368px;
    background: var(--navy);
    overflow: hidden;
  }
  .card--front { top: 46px; }
  .card--back { top: 437px; }

  .gold-text {
    background: var(--gold-gradient);
    -webkit-background-clip: text;
    background-clip: text;
    color: transparent;
  }

  .monogram {
    position: absolute;
    font-family: "Oswald", sans-serif;
    font-weight: 500;
    line-height: 1;
    white-space: nowrap;
  }
  .card--front .monogram {
    left: 27px;
    top: 17px;
    font-size: 60px;
  }
  .card--back .monogram {
    left: 0;
    right: 8px;
    top: 26px;
    text-align: center;
    font-size: 285px;
    letter-spacing: 4px;
    transform: scaleX(0.83);
    transform-origin: center;
  }

  .name {
    position: absolute;
    font-family: "Oswald", sans-serif;
    font-weight: 500;
    line-height: 1;
    text-transform: uppercase;
    white-space: nowrap;
  }
  .name--first {
    left: 114px;
    top: 21px;
    font-size: 29px;
  }
  .name--last {
    left: 103px;
    top: 56px;
    font-size: 26px;
  }
  .title {
    position: absolute;
    left: 29px;
    top: 88px;
    font-family: "Cinzel", serif;
    font-weight: 700;
    font-size: 22px;
    line-height: 1;
    letter-spacing: 3px;
    text-transform: uppercase;
    white-space: nowrap;
    transform: scaleX(1.6);
    transform-origin: left center;
  }
</style>
</head>
<body>
  <main class="sheet">
    <section class="card card--front" aria-label="Business card front">
      <span class="monogram gold-text">CV</span>
      <span class="name name--first gold-text">Camille</span>
      <span class="name name--last gold-text">Vautrin</span>
      <span class="title gold-text">Lawyer</span>
    </section>
    <section class="card card--back" aria-label="Business card back">
      <span class="monogram gold-text">CV</span>
    </section>
  </main>
</body>
</html>
```